Halvik Denatl Laboratory nees a window design

We want to make a window cover 8 feet wide and 6 feet tall to advertise our dental lab with all the products we produce<br/>: Digital Cad/Cam<br/>: Implants<br/>: Dentures<br/>: Cast Partials <br/>: Orthodontic appliances<br/><br/> and it has to include a service we provide for a denturist on site by appointment only.<br/><br/>Please use the sample logo below our colours are white backround and blue letters

Font styles to use
Script

Colors
ffffff
0355a3

Requirements
Nice to have
• a picture of a teddy bear on a dental chair, or some dental work particularly bridge work since our moto is Building bridges since 1976
Should not have
• real people

```html
<!DOCTYPE html>
<html lang="en">
<head>
<meta charset="utf-8">
<title>Halvik Denatl Laboratory – Window Cover</title>
<link rel="stylesheet" href="https://fonts.googleapis.com/css2?family=Exo+2:ital,wght@0,700;1,700&display=swap">
<style>
  :root {
    --brand-blue: #2a8acb;
    --deep-blue: #0355a3;
    --panel-grey: #f1f1f4;
    --white: #ffffff;
    --page-bg: #ffffff;
    --photo-light: #dcebf4;
    --photo-mid: #b9d6e8;
  }
  * { margin: 0; padding: 0; box-sizing: border-box; }
  html, body {
    width: 975px; height: 1200px; overflow: hidden;
    background: var(--page-bg);
    font-family: "Exo 2", "Arial", sans-serif;
  }
  .window-cover {
    position: absolute;
    left: 0; top: 234px;
    width: 975px; height: 731px;
    background: var(--white);
    overflow: hidden;
    box-shadow: 0 1px 4px rgba(0,0,0,0.25);
  }
  .cover-shapes { position: absolute; inset: 0; }
  .brand {
    position: absolute; left: 60px; top: 70px;
    display: flex; align-items: center; gap: 16px;
  }
  .brand-dot {
    width: 46px; height: 46px; border-radius: 50%;
    background: var(--brand-blue);
  }
  .brand-name {
    font-weight: 700; font-style: normal;
    font-size: 44px; line-height: 1;
    color: var(--brand-blue);
    letter-spacing: 0.5px;
  }
  .motto {
    position: absolute; right: 48px; top: 64px;
    text-align: right;
    font-weight: 700; font-style: italic;
    font-size: 20px; line-height: 28px;
    color: var(--brand-blue);
    text-transform: uppercase;
  }
  .products {
    position: absolute; left: 56px; top: 345px;
    color: var(--brand-blue);
    font-style: italic; font-weight: 700;
  }
  .products-title { font-size: 44px; line-height: 52px; }
  .products-list { list-style: none; font-size: 33px; line-height: 40px; }
  .products-list li::before { content: "• "; font-size: 28px; }
  .service-band {
    position: absolute; left: 0; top: 640px;
    width: 530px; height: 60px;
    background: linear-gradient(90deg, var(--brand-blue) 0%, var(--brand-blue) 55%, rgba(42,138,203,0) 100%);
    color: var(--white);
    font-style: italic; font-weight: 700;
    font-size: 19px; line-height: 24px;
    padding: 6px 0 0 50px;
  }
</style>
</head>
<body>
  <main class="window-cover">
    <svg class="cover-shapes" width="975" height="731" viewBox="0 0 975 731" aria-hidden="false">
      <defs>
        <linearGradient id="photoTone" x1="0" y1="0" x2="1" y2="1">
          <stop offset="0" stop-color="var(--photo-light)"/>
          <stop offset="0.6" stop-color="var(--photo-mid)"/>
          <stop offset="1" stop-color="#e9f2f7"/>
        </linearGradient>
      </defs>
      <circle class="photo-ring" cx="960" cy="690" r="470" fill="var(--brand-blue)"/>
      <circle class="photo-area" cx="960" cy="690" r="440" fill="url(#photoTone)" role="img" aria-label="Photo of a smiling dental patient in the chair during a check-up"/>
      <circle class="panel-ring" cx="230" cy="665" r="430" fill="var(--brand-blue)"/>
      <circle class="panel-fill" cx="212" cy="700" r="420" fill="var(--panel-grey)"/>
    </svg>

    <div class="brand">
      <span class="brand-dot"></span>
      <span class="brand-name">Halvik Denatl Laboratory</span>
    </div>

    <p class="motto">Building bridges<br>since 1976</p>

    <section class="products">
      <h2 class="products-title">PRODUCTS</h2>
      <ul class="products-list">
        <li>Digital Cad/Cam</li>
        <li>Implants</li>
        <li>Dentures</li>
        <li>Cast Partials</li>
        <li>Orthodontic appliances</li>
      </ul>
    </section>

    <p class="service-band">We provide a services for<br>denturist on site by appointment only</p>
  </main>
</body>
</html>
```